Business Card for Mortuary

We need a business card design for our mortuary. We are not the "traditional" mortuary and specialize in simple cremations and burials. We use a two sided card.

Industry/Entity Type

Funeral Home

Contact Information for Business Card

One side we would like to have with the general information of the mortuary:
Address: 4127 E. Larkspur Ave, Sun City, AZ 85399
Phone: 623-555-0142
email: hello@willowbendmortuary.example
website: willowbendmortuary.example

On the other side would like to have the information of employee:
Name: Mark T. Ellis
Email: mark@willowbendmortuary.example
Title: Funeral Director
Text: 602-555-0187

Font styles to use
Serif
Sans Serif

Requirements
Should not have
• Do not put any gothic images or things like a hearse or tombstone.

```html
<!DOCTYPE html>
<html lang="en">
<head>
<meta charset="utf-8">
<title>Willowbend Mortuary Business Cards</title>
<link rel="stylesheet" href="https://fonts.googleapis.com/css2?family=Montserrat:wght@700&family=Work+Sans:wght@400;500;600&display=swap">
<style>
  :root {
    --backdrop: #2f2f2f;
    --card: #ffffff;
    --card-shade: #e9e9e9;
    --ink: #1a1a1a;
    --ink-soft: #4a4a4a;
    --leaf-light: #b5d334;
    --leaf-mid: #8cc63f;
    --leaf-deep: #4fa843;
  }
  * { box-sizing: border-box; margin: 0; padding: 0; }
  html, body { width: 1038px; height: 1200px; overflow: hidden; }
  body {
    background: var(--backdrop);
    font-family: "Work Sans", Arial, sans-serif;
    color: var(--ink);
    position: relative;
  }
  .card {
    position: absolute;
    left: 69px;
    width: 900px;
    height: 513px;
    border-radius: 22px;
    overflow: hidden;
    background: var(--card);
    box-shadow: 0 6px 18px rgba(0,0,0,.45);
  }
  .card--staff { top: 58px; background: linear-gradient(180deg, var(--card) 35%, var(--card-shade) 100%); }
  .card--office { top: 629px; }

  .brand { position: absolute; top: 100px; display: flex; align-items: center; gap: 12px; }
  .brand__dot { width: 30px; height: 30px; border-radius: 50%; background: var(--leaf-mid); flex: none; }
  .brand__name {
    font-weight: 600; font-size: 30px; line-height: 1; color: var(--ink);
    letter-spacing: .5px; text-transform: uppercase; white-space: nowrap;
  }
  .card--staff .brand { left: 60px; }
  .card--office .brand { right: 54px; }

  .person { position: absolute; left: 60px; top: 240px; }
  .person__name { font-family: "Montserrat", Arial, sans-serif; font-weight: 700; font-size: 32px; letter-spacing: .5px; }
  .person__title { font-size: 23px; color: var(--ink-soft); margin-top: 4px; letter-spacing: .5px; }

  .contact { position: absolute; list-style: none; font-size: 23px; color: var(--ink-soft); letter-spacing: .4px; }
  .contact li { display: flex; align-items: center; gap: 6px; height: 33px; }
  .card--staff .contact { left: 60px; top: 360px; }
  .card--office .contact { right: 52px; top: 360px; }
  .card--office .contact li { justify-content: flex-end; }

  .icon { width: 22px; height: 22px; flex: none; }

  .address { position: absolute; right: 54px; top: 245px; text-align: right; font-size: 23px; line-height: 1.4; color: var(--ink-soft); letter-spacing: .4px; }

  .leaf-art { position: absolute; }
  .card--staff .leaf-art {
    right: 0; bottom: 0; width: 350px; height: 513px;
    border-top-left-radius: 100% 70%;
    background: linear-gradient(160deg, var(--leaf-light) 0%, var(--leaf-mid) 55%, var(--leaf-deep) 100%);
    opacity: .9;
  }
  .card--office .leaf-art {
    left: 0; top: 0; width: 215px; height: 513px;
    border-bottom-right-radius: 100% 80%;
    border-top-right-radius: 40% 30%;
    background: linear-gradient(200deg, var(--leaf-light) 0%, var(--leaf-mid) 60%, var(--leaf-deep) 100%);
    opacity: .9;
  }
</style>
</head>
<body>

<svg width="0" height="0" style="position:absolute">
  <defs>
    <symbol id="icon-phone" viewBox="0 0 22 22">
      <circle cx="11" cy="11" r="10" fill="none" stroke="#8cc63f" stroke-width="2"/>
      <circle cx="11" cy="11" r="7" fill="#8cc63f"/>
      <path d="M8 7.5c.6-.6 1.2-.3 1.5.3l.5 1c.2.4 0 .8-.3 1l-.4.3c.4.9 1.1 1.6 2 2l.3-.4c.3-.3.6-.5 1-.3l1 .5c.6.3.9.9.3 1.5-1.6 1.6-6.6-3.4-5.9-5.9z" fill="#fff"/>
    </symbol>
    <symbol id="icon-mail" viewBox="0 0 22 22">
      <circle cx="11" cy="11" r="10" fill="none" stroke="#8cc63f" stroke-width="2"/>
      <circle cx="11" cy="11" r="7" fill="#8cc63f"/>
      <rect x="7" y="8.5" width="8" height="5.5" rx=".6" fill="#fff"/>
      <path d="M7.3 9l3.7 2.6L14.7 9" fill="none" stroke="#8cc63f" stroke-width=".9"/>
    </symbol>
    <symbol id="icon-web" viewBox="0 0 22 22">
      <circle cx="11" cy="11" r="10" fill="none" stroke="#8cc63f" stroke-width="2"/>
      <circle cx="11" cy="11" r="7" fill="#8cc63f"/>
      <circle cx="11" cy="11" r="4" fill="none" stroke="#fff" stroke-width="1"/>
      <path d="M7 11h8M11 7c-1.6 2.4-1.6 5.6 0 8M11 7c1.6 2.4 1.6 5.6 0 8" fill="none" stroke="#fff" stroke-width=".8"/>
    </symbol>
  </defs>
</svg>

<section class="card card--staff">
  <div class="leaf-art" role="img" aria-label="Large overlapping green leaf decoration"></div>
  <div class="brand">
    <span class="brand__dot"></span>
    <span class="brand__name">Willowbend Mortuary</span>
  </div>
  <div class="person">
    <p class="person__name">MARK T. ELLIS</p>
    <p class="person__title">Funeral Director</p>
  </div>
  <ul class="contact">
    <li><svg class="icon"><use href="#icon-phone"/></svg>602-555-0187</li>
    <li><svg class="icon"><use href="#icon-mail"/></svg>mark@willowbendmortuary.example</li>
    <li><svg class="icon"><use href="#icon-web"/></svg>willowbendmortuary.example</li>
  </ul>
</section>

<section class="card card--office">
  <div class="leaf-art" role="img" aria-label="Large green leaf decoration along the left edge"></div>
  <div class="brand">
    <span class="brand__dot"></span>
    <span class="brand__name">Willowbend Mortuary</span>
  </div>
  <p class="address">4127 E. Larkspur<br>Ave, Sun City, AZ 85399</p>
  <ul class="contact">
    <li>623-555-0142<svg class="icon"><use href="#icon-phone"/></svg></li>
    <li>hello@willowbendmortuary.example<svg class="icon"><use href="#icon-mail"/></svg></li>
    <li>willowbendmortuary.example<svg class="icon"><use href="#icon-web"/></svg></li>
  </ul>
</section>

</body>
</html>
```